Professional Package for CPA Firm

We would like a stationery design for our new CPA Firm based in Atlanta, GA called 'Vale 7'. We work with investors to help grow investments, tax free. We would like the design to have a professional/minimal look with a 'wow' factor. We need 9.5″ x 4.125″, 9x12, and 10x13 mailing envelopes, business cards, and a letterhead. We have a logo that is already complete. For the letterhead, we would like to have space to put credentials at the bottom of the page

Industry/Entity Type

CPA, Accounting

```html
<!DOCTYPE html>
<html lang="en">
<head>
<meta charset="utf-8">
<title>Vale 7 — Business Card</title>
<link href="https://fonts.googleapis.com/css2?family=Lato:wght@400;700&display=swap" rel="stylesheet">
<style>
  :root {
    --backdrop: #dcd8d1;
    --panel-dark: #0e151a;
    --panel-mid: #283540;
    --frost-light: #eef0f0;
    --frost-shade: #cfd4d5;
    --teal: #2b8290;
    --teal-line: #1f7c88;
    --text-light: #e4e8ea;
    --brand-ink: #161d24;
  }
  * { margin: 0; padding: 0; box-sizing: border-box; }
  html, body { width: 1200px; height: 969px; overflow: hidden; }
  body {
    background: var(--backdrop);
    font-family: "Lato", Arial, sans-serif;
    position: relative;
  }
  .business-card {
    position: absolute;
    left: 100px; top: 200px;
    width: 1000px; height: 570px;
    border-radius: 28px;
    overflow: hidden;
    background: linear-gradient(160deg, var(--frost-light), var(--frost-shade));
    box-shadow: 0 10px 30px rgba(0,0,0,0.18);
  }
  .card-shape { position: absolute; inset: 0; }
  .contact-block {
    position: absolute;
    left: 58px; top: 126px;
    color: var(--text-light);
  }
  .person-name {
    font-size: 31px; font-weight: 700;
    color: var(--teal); letter-spacing: 0.5px;
    line-height: 1.1;
  }
  .person-role { font-size: 21px; margin-top: 4px; }
  .address { font-size: 21px; line-height: 28px; margin-top: 40px; }
  .contact-list { list-style: none; margin-top: 18px; }
  .contact-list li {
    display: flex; align-items: center;
    font-size: 21px; height: 28.5px;
  }
  .contact-list svg { width: 18px; height: 18px; margin-right: 14px; fill: var(--teal); flex: none; }
  .brand-block {
    position: absolute;
    left: 618px; top: 300px; width: 320px;
    text-align: center;
    color: var(--brand-ink);
  }
  .brand-name {
    font-size: 64px; font-weight: 700; letter-spacing: 3px; line-height: 1;
  }
  .brand-tagline {
    font-size: 17px; font-weight: 700; letter-spacing: 1.2px; margin-top: 8px;
  }
</style>
</head>
<body>
  <div class="business-card">
    <svg class="card-shape" viewBox="0 0 1000 570" width="1000" height="570" aria-hidden="true">
      <defs>
        <radialGradient id="darkPanel" cx="0.25" cy="0.55" r="0.75">
          <stop offset="0" stop-color="var(--panel-mid)"/>
          <stop offset="1" stop-color="var(--panel-dark)"/>
        </radialGradient>
      </defs>
      <path d="M0 0 H659 L412 268 Q398 285 412 302 L670 570 H0 Z" fill="url(#darkPanel)"/>
      <path d="M682 -4 L434 268 Q420 285 434 302 L694 574" fill="none" stroke="var(--teal-line)" stroke-width="6"/>
      <path d="M668 -4 L420 268 Q406 285 420 302 L680 574" fill="none" stroke="#ffffff" stroke-opacity="0.35" stroke-width="1.5"/>
    </svg>

    <div class="contact-block">
      <div class="person-name">DANIEL REYES</div>
      <div class="person-role">President</div>
      <div class="address">4812 Birchwood Lane<br>Fairbanks, Alaska 34518</div>
      <ul class="contact-list">
        <li><svg viewBox="0 0 24 24"><path d="M6.6 10.8a15 15 0 0 0 6.6 6.6l2.2-2.2a1 1 0 0 1 1-.25 11.4 11.4 0 0 0 3.6.57 1 1 0 0 1 1 1V20a1 1 0 0 1-1 1A17 17 0 0 1 3 4a1 1 0 0 1 1-1h3.5a1 1 0 0 1 1 1c0 1.25.2 2.45.57 3.6a1 1 0 0 1-.25 1z"/></svg>555-214-7730</li>
        <li><svg viewBox="0 0 24 24"><path d="M7 1h10a2 2 0 0 1 2 2v18a2 2 0 0 1-2 2H7a2 2 0 0 1-2-2V3a2 2 0 0 1 2-2zm0 3v14h10V4zm5 15.5a1 1 0 1 0 0 2 1 1 0 0 0 0-2z"/></svg>555-863-4102</li>
        <li><svg viewBox="0 0 24 24"><path d="M3 5h18v14H3zm2 2v.5l7 4.5 7-4.5V7zm0 2.8V17h14V9.8l-7 4.5z"/></svg>info@vale7.com</li>
        <li><svg viewBox="0 0 24 24"><path d="M12 2a10 10 0 1 0 0 20 10 10 0 0 0 0-20zm-1 17.9A8 8 0 0 1 4.2 10.4L9 15v1a2 2 0 0 0 2 2zm6.9-2.5A2 2 0 0 0 16 16h-1v-3a1 1 0 0 0-1-1H8v-2h2a1 1 0 0 0 1-1V7h2a2 2 0 0 0 2-2v-.4a8 8 0 0 1 2.9 12.8z"/></svg>www.vale7.com</li>
      </ul>
    </div>

    <div class="brand-block">
      <div class="brand-name">VALE 7</div>
      <div class="brand-tagline">CPAs and Tax Advisors</div>
    </div>
  </div>
</body>
</html>
```